New Hand Swiss Brewery needs labels

I need labels for un brand new brewery created in Switzerland called "Brasserie du Galet". The name reflects two things: the air bubbles (CO2) present in beer and the low alcohol level content. I'm brewing a base of 3 types: a refreshing and aromatic american blond, a malty sweet red ale and a German dark wheat beer with character. The beers names are not yet defined but should be on the front mixed up the design. The label should be in one piece with the back containing the information on the ingredients and other informations. The bottles are with à long neck and black (image attached).
Updates

Project Deadline Extended Reason: I still can not decide ... I need a little more proposals or/and improvements !I will reply to messages shortlygreetings and thanks for your work... Added Monday, May 16, 2016

Target Market(s)

Regional

Industry/Entity Type

Brewery

Requirements
Must have
• Ingrédients informations on the back: exemple for the Dark wheat beer
• - IBU (international bitterness unit): 21.9
• - Couleur EBC (color): 36.4
• - Malts: Pilsner, froment, froment caramel, froment grillé, velutto
• - Houblons: Felsora Tundin, Morrowick
• - Levure allemande de fermentation haute
• - Contient: Eau, Malts, houblons, levures
Nice to have
• I like asymmetric style modern graphics. It could be lines and shapes for exemple. Even drawing like comics could be a great idea.

```html
<!DOCTYPE html>
<html lang="en">
<head>
<meta charset="utf-8">
<title>Brasserie du Galet – German Dark Wheat Beer label</title>
<link rel="stylesheet" href="https://fonts.googleapis.com/css2?family=Advent+Pro:wght@300;400&display=swap">
<style>
  :root {
    --page: #ffffff;
    --label-black: #050505;
    --swirl-tone: #1c1c1c;
    --ink-grey: #cfcfcf;
    --rule-grey: #bdbdbd;
  }
  html, body {
    margin: 0;
    padding: 0;
    width: 720px;
    height: 1200px;
    overflow: hidden;
    background: var(--page);
  }
  .label {
    position: relative;
    width: 720px;
    height: 1200px;
    background: var(--label-black);
    overflow: hidden;
    font-family: "Advent Pro", "Arial Narrow", sans-serif;
    color: var(--ink-grey);
  }
  .swirl-texture {
    position: absolute;
    inset: 0;
    background:
      radial-gradient(ellipse 40% 35% at 88% 30%, var(--swirl-tone), transparent 70%),
      radial-gradient(ellipse 40% 30% at 15% 18%, #121212, transparent 70%),
      radial-gradient(ellipse 45% 35% at 85% 78%, #181818, transparent 70%),
      var(--label-black);
  }
  .diagonal-rule {
    position: absolute;
    inset: 0;
  }
  .brand-mark {
    position: absolute;
    left: 350px;
    top: 246px;
    display: flex;
    align-items: center;
    gap: 12px;
    font-weight: 400;
    font-size: 32px;
    line-height: 1;
    letter-spacing: 0.5px;
    text-transform: uppercase;
    color: var(--ink-grey);
    white-space: nowrap;
  }
  .brand-mark .mark-square {
    width: 20px;
    height: 20px;
    background: var(--ink-grey);
  }
  .label-text {
    position: absolute;
    left: 2px;
    top: 680px;
    text-transform: uppercase;
    white-space: nowrap;
  }
  .brewery-name {
    margin: 0;
    font-weight: 400;
    font-size: 44px;
    line-height: 1;
    letter-spacing: 0.3px;
  }
  .beer-style,
  .tagline {
    margin: 0;
    font-weight: 400;
    font-size: 28px;
    line-height: 1;
  }
  .beer-style { margin-top: 22px; }
  .tagline { margin-top: 16px; }
</style>
</head>
<body>
  <main class="label">
    <div class="swirl-texture" role="img" aria-label="Dark marbled swirl texture covering the black label"></div>

    <svg class="diagonal-rule" width="720" height="1200" viewBox="0 0 720 1200" aria-hidden="true">
      <line x1="158" y1="157" x2="474" y2="842" stroke="var(--rule-grey)" stroke-width="2.5"/>
    </svg>

    <div class="brand-mark">
      <span class="mark-square"></span>
      <span>Brasserie du Galet</span>
    </div>

    <section class="label-text">
      <h1 class="brewery-name">Brasserie du Galet</h1>
      <p class="beer-style">German Dark Wheat Beer</p>
      <p class="tagline">Drink Brave</p>
    </section>
  </main>
</body>
</html>
```